ORVALO Global Commerce Inc.
Kareem Bin-Sahwan
Vice President
Unit 385, 2096 Pellmore Crescent Toronto, Ontario, Canada M4R 2K6
kareem@orvaloglobal.ca
www.orvaloglobal.ca
The company's name is "ORVALO Global Commerce Inc." The company's new logo is only stating ORVALO, i need the wording "Global Commerce Inc." to be added next to the logo at different designs for me to choose from.
The logo of the company with the wording "Global Commerce Inc." at different backgrounds and design for me to choose from.

```html
<!DOCTYPE html>
<html lang="en">
<head>
<meta charset="utf-8">
<title>ORVALO Global Commerce Inc. – Business Card</title>
<link href="https://fonts.googleapis.com/css2?family=Montserrat:wght@300;400;600;700&display=swap" rel="stylesheet">
<style>
  :root {
    --brand-blue: #2f86bf;
    --brand-grey: #3d3f44;
    --ink: #2a2c30;
    --muted: #6b6e74;
    --card: #ffffff;
    --backdrop: #e9e6e1;
  }
  * { box-sizing: border-box; margin: 0; padding: 0; }
  html, body { width: 1200px; height: 996px; overflow: hidden; }
  body {
    background: var(--backdrop);
    font-family: "Montserrat", sans-serif;
    color: var(--ink);
    display: flex;
    flex-direction: column;
    align-items: center;
    justify-content: center;
    gap: 40px;
  }
  .card {
    position: relative;
    width: 760px;
    height: 434px;
    background: var(--card);
    border-radius: 14px;
    overflow: hidden;
    box-shadow: 0 10px 30px rgba(0,0,0,.18);
  }
  .card-waves { position: absolute; inset: 0; width: 100%; height: 100%; }
  .wordmark {
    position: absolute;
    display: flex;
    align-items: center;
    gap: 12px;
    font-weight: 700;
    color: var(--brand-grey);
    letter-spacing: .06em;
  }
  .wordmark-square { background: var(--brand-blue); }
  .card-front .wordmark { left: 56px; top: 70px; font-size: 58px; }
  .card-front .wordmark-square { width: 16px; height: 16px; }
  .tagline {
    position: absolute; left: 58px; top: 146px;
    font-size: 14px; font-weight: 400; color: var(--muted); letter-spacing: .12em;
  }
  .holder { position: absolute; right: 56px; top: 70px; text-align: right; }
  .holder-name { font-size: 22px; font-weight: 600; letter-spacing: .04em; text-transform: uppercase; }
  .holder-title { font-size: 13px; color: var(--muted); margin-top: 4px; letter-spacing: .08em; }
  .contacts { position: absolute; right: 56px; top: 148px; list-style: none; }
  .contacts li {
    display: flex; justify-content: flex-end; align-items: center; gap: 10px;
    font-size: 13px; line-height: 26px; color: var(--ink);
  }
  .contact-icon { width: 14px; height: 14px; fill: var(--brand-blue); }
  .address {
    position: absolute; left: 58px; bottom: 58px;
    font-size: 13px; line-height: 20px; color: var(--ink); max-width: 300px;
  }
  .card-back .wordmark { left: 330px; top: 172px; font-size: 78px; }
  .card-back .wordmark-square { width: 20px; height: 20px; }
</style>
</head>
<body>

<section class="card card-front" aria-label="Business card front">
  <svg class="card-waves" viewBox="0 0 760 434" preserveAspectRatio="none" aria-hidden="true">
    <path d="M300,434 C480,420 640,360 760,250 L760,270 C640,380 480,430 340,434 Z" fill="var(--brand-grey)"/>
    <path d="M360,434 C510,426 650,380 760,292 L760,434 Z" fill="var(--brand-blue)"/>
  </svg>
  <div class="wordmark"><span class="wordmark-square"></span>ORVALO</div>
  <p class="tagline">Global Commerce Inc.</p>
  <div class="holder">
    <p class="holder-name">Kareem Bin-Sahwan</p>
    <p class="holder-title">Vice President</p>
  </div>
  <ul class="contacts">
    <li>+1 416 555 0142
      <svg class="contact-icon" viewBox="0 0 24 24"><path d="M6.6 10.8a15 15 0 0 0 6.6 6.6l2.2-2.2c.3-.3.7-.4 1-.2 1.1.4 2.3.6 3.6.6.6 0 1 .4 1 1V20c0 .6-.4 1-1 1A17 17 0 0 1 3 4c0-.6.4-1 1-1h3.5c.6 0 1 .4 1 1 0 1.3.2 2.5.6 3.6.1.3 0 .7-.2 1z"/></svg></li>
    <li>+1 416 555 0143
      <svg class="contact-icon" viewBox="0 0 24 24"><path d="M6 3h10v5H6zM4 9h16a1 1 0 0 1 1 1v7h-3v4H6v-4H3v-7a1 1 0 0 1 1-1zm4 7v3h8v-3z"/></svg></li>
    <li>kareem@orvaloglobal.ca
      <svg class="contact-icon" viewBox="0 0 24 24"><path d="M3 5h18v14H3zm2 2v.5l7 4.5 7-4.5V7z"/></svg></li>
    <li>www.orvaloglobal.ca
      <svg class="contact-icon" viewBox="0 0 24 24"><circle cx="12" cy="12" r="9" fill="none" stroke="var(--brand-blue)" stroke-width="2"/><path d="M3 12h18M12 3c3 3 3 15 0 18M12 3c-3 3-3 15 0 18" fill="none" stroke="var(--brand-blue)" stroke-width="1.6"/></svg></li>
  </ul>
  <p class="address">Unit 385, 2096 Pellmore Crescent<br>Toronto, Ontario, Canada M4R 2K6</p>
</section>

<section class="card card-back" aria-label="Business card back">
  <svg class="card-waves" viewBox="0 0 760 434" preserveAspectRatio="none" aria-hidden="true">
    <path d="M0,0 L150,0 C80,140 110,300 300,434 L270,434 C80,310 50,150 120,0 Z" fill="var(--brand-grey)"/>
    <path d="M0,0 L110,0 C40,150 70,310 250,434 L0,434 Z" fill="var(--brand-blue)"/>
  </svg>
  <div class="wordmark"><span class="wordmark-square"></span>ORVALO</div>
</section>

</body>
</html>
```